Marrow Creek Outdoors League needs a poster for fish fry

We need a flyer made for a fish fry. Things we need on it;

Date: Sunday, February 12th
Location: Brennock Sportsdome Hall
Time: 5-6:30 pm
Cost: $15 for adults, $10 for 12 & under, free for preschool

Requirements
Must have
• Must have our logo on it.

```html
<!DOCTYPE html>
<html lang="en">
<head>
<meta charset="utf-8">
<title>Fish Fry – Marrow Creek Outdoors League</title>
<link href="https://fonts.googleapis.com/css2?family=Poppins:wght@400;500;700;800&family=Passion+One:wght@700&family=Kaushan+Script&family=Caveat+Brush&family=Bebas+Neue&display=swap" rel="stylesheet">
<style>
  :root{
    --ink:#141414;
    --night:#1c1c1c;
    --orange:#f7960f;
    --white:#ffffff;
    --paper:#e4e4e4;
    --teal:#2e7b88;
    --wood:#6b3f22;
    --fish:#b07a3e;
  }
  *{margin:0;padding:0;box-sizing:border-box}
  html,body{width:1200px;height:1200px;overflow:hidden;background:var(--white)}
  .canvas{position:relative;width:1200px;height:1200px;background:var(--white)}
  .flyer{
    position:absolute;left:238px;top:104px;width:757px;height:981px;overflow:hidden;
    background:radial-gradient(ellipse at 40% 40%, #262626 0%, var(--night) 55%, #121212 100%);
    font-family:"Poppins",sans-serif;color:var(--white);
  }
  .smoke{position:absolute;right:-40px;top:-10px;width:230px;height:220px;
    background:radial-gradient(ellipse at 60% 45%, rgba(190,190,190,.45) 0%, rgba(120,120,120,.18) 45%, rgba(0,0,0,0) 72%)}
  .hero-photo{position:absolute;left:420px;top:215px;width:420px;height:340px;border-radius:26px;
    transform:rotate(-38deg);transform-origin:30% 50%;
    background:linear-gradient(135deg, var(--wood) 0%, #8a5a32 30%, var(--fish) 50%, #4a2a1c 78%, #2b1a12 100%)}
  .brand{position:absolute;left:88px;top:72px;width:170px;text-align:center}
  .brand-dot{width:26px;height:26px;border-radius:50%;background:var(--white);margin:0 auto 12px}
  .brand-name{font-family:"Poppins",sans-serif;font-weight:700;font-size:17px;line-height:1.2;color:var(--white);letter-spacing:.5px}
  .date-badge{position:absolute;left:414px;top:93px;width:200px;height:200px;border-radius:50%;
    background:var(--ink);border:3px dashed var(--white);text-align:center;padding-top:28px}
  .date-day{font-family:"Bebas Neue",sans-serif;font-size:58px;line-height:1;color:var(--orange);letter-spacing:1px}
  .date-month{font-family:"Poppins",sans-serif;font-weight:800;font-size:21px;line-height:1.2;letter-spacing:1px;margin-top:2px}
  .date-weekday{font-family:"Caveat Brush",sans-serif;font-size:42px;line-height:1;transform:skewX(-8deg);margin-top:0}
  .title-script{position:absolute;left:40px;top:240px;font-family:"Kaushan Script",cursive;font-size:150px;line-height:1;color:var(--white);z-index:2}
  .title-block{position:absolute;left:36px;top:316px;font-family:"Passion One",sans-serif;font-weight:700;font-size:260px;line-height:1;color:var(--orange);letter-spacing:0;
    transform:scaleX(.84);transform-origin:left top}
  .sparks{position:absolute;left:0;top:0;width:757px;height:600px;pointer-events:none}
  .price{position:absolute;left:49px;width:341px;height:40px;border-radius:20px;background:var(--ink);display:flex;align-items:center}
  .price-label{padding-left:26px;font-weight:800;font-size:19px;letter-spacing:.6px;flex:1}
  .price-tag{width:116px;height:40px;border-radius:20px;background:var(--orange);color:var(--ink);
    font-weight:800;font-size:30px;display:flex;align-items:center;justify-content:center}
  .price--adult{top:570px}
  .price--child{top:636px}
  .free-stroke{position:absolute;left:462px;top:572px;width:284px;height:132px}
  .free-text{position:absolute;left:512px;top:586px;color:var(--ink);text-align:left}
  .free-big{font-family:"Poppins",sans-serif;font-weight:800;font-size:64px;line-height:1;letter-spacing:2px}
  .free-small{font-weight:800;font-size:16px;line-height:1;letter-spacing:.6px;margin-top:4px;white-space:nowrap}
  .info-band{position:absolute;left:0;top:718px;width:757px;height:263px}
  .plate-photo{position:absolute;left:-30px;top:716px;width:295px;height:265px;border-radius:0 150px 150px 0;
    background:radial-gradient(ellipse at 45% 50%, #7a3b1c 0%, #5a2a14 40%, #3f6b2a 75%, #f2f2f2 78%, #ffffff 100%)}
  .info{position:absolute;left:303px;color:var(--ink)}
  .info-tag{display:inline-block;background:var(--orange);color:var(--ink);font-size:14px;font-weight:500;
    padding-left:11px;height:17px;line-height:17px;border-radius:4px 10px 4px 4px}
  .info--location .info-tag{width:112px}
  .info--time .info-tag{width:83px}
  .info-text{font-size:14px;font-weight:500;margin-top:6px;letter-spacing:.3px}
  .info-text--bold{font-weight:700;font-size:17px}
  .info--location{top:803px}
  .info--time{top:879px}
  .quality-seal{position:absolute;left:556px;top:791px;width:160px;height:160px}
</style>
</head>
<body>
<div class="canvas">
  <article class="flyer">
    <div class="smoke" role="img" aria-label="Rising steam"></div>
    <div class="hero-photo" role="img" aria-label="Photo of grilled fish with lemon slices and eggplant on a wooden board"></div>

    <div class="brand">
      <div class="brand-dot"></div>
      <div class="brand-name">Marrow Creek Outdoors League</div>
    </div>

    <div class="date-badge">
      <div class="date-day">12TH</div>
      <div class="date-month">FEBRUARY</div>
      <div class="date-weekday">SUNDAY</div>
    </div>

    <svg class="sparks" viewBox="0 0 757 600" aria-hidden="true">
      <polygon points="45,205 72,192 78,212" fill="var(--orange)"/>
      <polygon points="40,225 62,220 56,234" fill="var(--white)"/>
      <polygon points="82,188 90,186 86,210" fill="var(--white)"/>
      <polygon points="378,495 402,486 404,498" fill="var(--white)"/>
      <polygon points="382,514 410,508 402,524" fill="var(--orange)"/>
      <polygon points="376,532 388,528 398,548" fill="var(--white)"/>
    </svg>

    <div class="title-block">FRY</div>
    <div class="title-script">Fish</div>

    <div class="price price--adult"><span class="price-label">FOR ADULTS</span><span class="price-tag">$15</span></div>
    <div class="price price--child"><span class="price-label">FOR 12 &amp; UNDER</span><span class="price-tag">$10</span></div>

    <svg class="free-stroke" viewBox="0 0 284 132" aria-hidden="true">
      <path d="M16,18 L236,6 L262,34 L282,92 L250,100 L270,112 L170,108 L70,114 L14,130 L8,106 L20,92 L2,70 L14,46 L0,30 Z" fill="var(--orange)"/>
    </svg>
    <div class="free-text">
      <div class="free-big">FREE</div>
      <div class="free-small">FOR PRESCHOOL</div>
    </div>

    <svg class="info-band" viewBox="0 0 757 263" preserveAspectRatio="none" aria-hidden="true">
      <path d="M0,10 L60,6 L120,18 L200,4 L260,16 L330,8 L400,22 L470,10 L540,26 L610,14 L680,30 L757,20 L757,263 L0,263 Z" fill="var(--paper)"/>
    </svg>
    <div class="plate-photo" role="img" aria-label="Photo of spiced fried fish on a plate with onion and tomato"></div>

    <div class="info info--location">
      <span class="info-tag">LOCATION:</span>
      <p class="info-text">BRENNOCK SPORTSDOME HALL</p>
    </div>
    <div class="info info--time">
      <span class="info-tag">TIME:</span>
      <p class="info-text info-text--bold">5-6:30 PM</p>
    </div>

    <svg class="quality-seal" viewBox="0 0 160 160" aria-hidden="true">
      <circle cx="80" cy="80" r="76" fill="none" stroke="var(--teal)" stroke-width="4"/>
      <circle cx="80" cy="80" r="54" fill="none" stroke="var(--teal)" stroke-width="2"/>
    </svg>
  </article>
</div>
</body>
</html>
```